Top Service Company - Inside Back Cover of VELK Journal Ad -

We need a full page ad that can also be expanded into a full two page - For Top Residential Services Company - RQW Sparkle is the Largest in the country (UAE) Moro Mend Up, (Maintenance, Pest Control, AC Duct Cleaning and Remodeling)

Please see all logos attached
There are two pervious fliers for EXAMPLE ONLY - do NOT want something that looks the same - want new & fresh!

Target Market(s)

Families, Airport Lounges, Hotels and Airline travelers will all view this Magazine.

Industry/Entity Type

Residential

Font styles to use
Serif

Colors

Designer to choose colors to be used in the design.

Requirements
Must have
• Sizes
• Double Page Spread Advert
• (DPS) 265mm (h) x 448mm (w)
• Full Page Specs:
• Ø Trim W200 x H265 mm
• Ø Bleed W210 x H275 mm
• Ø Type W195 x H250 mm
• Bleed
• Artwork for all adverts must include a 5mm bleed on all sides (see sizes above), all text and images should be at least a further 5mm from the crop guides. The easiest way of thinking of this if you are uncertain is to ensure the
• background image goes to right to the edge of the file and then all text, logos, etc are at least 8mm from the edges. To ensure correct printing an appropriate border will be added to all artwork supplied without correct bleeds.
• Colour
• Artwork should be completed and saved in CMYK process, Please delete all unused colour swatches from the colour palettes. Do not use Pantone or similar colours
Nice to have
• Clean - easy to read -
• Bright Colors
• Should be different

```html
<!DOCTYPE html>
<html lang="en">
<head>
<meta charset="utf-8">
<title>RQW Sparkle &amp; Moro Mend Up Double Page Spread</title>
<link href="https://fonts.googleapis.com/css2?family=Playfair+Display:wght@700&family=Source+Serif+4:wght@400;600&display=swap" rel="stylesheet">
<style>
:root{
  --navy:#143d6b;
  --navy-deep:#0f2f54;
  --green:#5fa83a;
  --red:#c0272d;
  --cream:#fbf8f2;
  --white:#ffffff;
  --ink:#2a3a4e;
  --stage:#e6e6e6;
}
*{margin:0;padding:0;box-sizing:border-box}
html,body{width:1200px;height:863px;overflow:hidden}
body{background:var(--stage);position:relative;font-family:"Source Serif 4",serif}
.spread{position:absolute;left:40px;top:100px;width:1120px;height:662px;background:var(--cream);overflow:hidden;box-shadow:0 6px 18px rgba(0,0,0,.22)}
.page{position:absolute;top:0;width:560px;height:612px}
.page--cleaning{left:0}
.page--maintenance{left:560px}
.gutter{position:absolute;left:559px;top:0;width:2px;height:612px;background:linear-gradient(90deg,rgba(0,0,0,.12),rgba(0,0,0,0))}
.photo{position:absolute;left:0;top:0;width:560px;height:330px}
.photo--cleaning{background:linear-gradient(155deg,#f4f7f8 0%,#d4e6ea 40%,#9cc7cf 70%,#e9d878 100%)}
.photo--maintenance{background:linear-gradient(120deg,#5f7ea6 0%,#c9a45e 45%,#e4cb93 70%,#f1ebde 100%)}
.photo-edge{position:absolute;left:0;top:322px;width:560px;height:8px}
.page--cleaning .photo-edge{background:var(--green)}
.page--maintenance .photo-edge{background:var(--red)}
.brand{position:absolute;top:28px;height:52px;padding:0 18px;background:var(--white);border-radius:6px;display:flex;align-items:center;gap:10px;box-shadow:0 2px 8px rgba(0,0,0,.12)}
.page--cleaning .brand{left:36px}
.page--maintenance .brand{right:36px}
.brand-mark{width:16px;height:16px;border-radius:50%}
.page--cleaning .brand-mark{background:var(--green)}
.page--maintenance .brand-mark{background:var(--red)}
.brand-name{font-family:"Source Serif 4",serif;font-weight:600;font-size:20px;color:var(--navy)}
.kicker{position:absolute;left:36px;top:352px;font-size:13px;font-weight:600;letter-spacing:3px;text-transform:uppercase}
.page--cleaning .kicker{color:var(--green)}
.page--maintenance .kicker{color:var(--red)}
.headline{position:absolute;left:36px;top:372px;font-family:"Playfair Display",serif;font-weight:700;font-size:34px;line-height:40px;color:var(--navy)}
.features{position:absolute;left:36px;top:474px;width:488px;list-style:none;display:grid;grid-template-columns:1fr 1fr;row-gap:6px;font-size:16px;line-height:20px;color:var(--ink)}
.features li{display:flex;align-items:center;gap:8px}
.features svg{flex:none}
.copy{position:absolute;left:36px;top:540px;width:488px;font-size:14px;line-height:20px;color:var(--ink)}
.badge{position:absolute;left:424px;top:262px;width:112px;height:112px;border-radius:50%;background:var(--red);border:4px solid var(--white);display:flex;flex-direction:column;align-items:center;justify-content:center;color:var(--white);text-align:center;box-shadow:0 3px 10px rgba(0,0,0,.2)}
.badge-num{font-family:"Playfair Display",serif;font-weight:700;font-size:34px;line-height:34px}
.badge-label{font-size:11px;font-weight:600;letter-spacing:1.5px;line-height:14px}
.footer{position:absolute;left:0;top:612px;width:1120px;height:50px;background:var(--navy-deep);display:flex;align-items:center;justify-content:space-between;padding:0 36px}
.footer-call{font-family:"Playfair Display",serif;font-weight:700;font-size:20px;color:var(--white);letter-spacing:.5px}
.footer-phone{display:flex;align-items:center;gap:10px;height:34px;padding:0 18px;border-radius:17px;background:var(--green);font-family:"Source Serif 4",serif;font-weight:600;font-size:19px;color:var(--white)}
</style>
</head>
<body>
<main class="spread">

  <section class="page page--cleaning">
    <div class="photo photo--cleaning" role="img" aria-label="Housekeeper in yellow gloves cleaning a bright living room"></div>
    <div class="photo-edge"></div>
    <div class="brand"><span class="brand-mark"></span><span class="brand-name">RQW Sparkle</span></div>
    <p class="kicker">Home Cleaning</p>
    <h1 class="headline">A spotless home,<br>every single visit.</h1>
    <ul class="features">
      <li><svg width="14" height="12" viewBox="0 0 14 12"><path d="M1 6 L5 10 L13 1" stroke="var(--green)" stroke-width="3" fill="none"/></svg>Same maid every time</li>
      <li><svg width="14" height="12" viewBox="0 0 14 12"><path d="M1 6 L5 10 L13 1" stroke="var(--green)" stroke-width="3" fill="none"/></svg>Ironing &amp; laundry</li>
      <li><svg width="14" height="12" viewBox="0 0 14 12"><path d="M1 6 L5 10 L13 1" stroke="var(--green)" stroke-width="3" fill="none"/></svg>In-house training facility</li>
      <li><svg width="14" height="12" viewBox="0 0 14 12"><path d="M1 6 L5 10 L13 1" stroke="var(--green)" stroke-width="3" fill="none"/></svg>Endorsed by the UAE government</li>
    </ul>
    <p class="copy">The largest residential cleaning team in the UAE, with qualified maids trained in our own facility.</p>
  </section>

  <div class="gutter"></div>

  <section class="page page--maintenance">
    <div class="photo photo--maintenance" role="img" aria-label="Technician with a tool belt servicing an air conditioning unit"></div>
    <div class="photo-edge"></div>
    <div class="brand"><span class="brand-mark"></span><span class="brand-name">Moro Mend Up</span></div>
    <div class="badge"><span class="badge-num">24</span><span class="badge-label">HOUR<br>SERVICE</span></div>
    <p class="kicker">Home Maintenance</p>
    <h2 class="headline">Your property,<br>our priority.</h2>
    <ul class="features">
      <li><svg width="14" height="12" viewBox="0 0 14 12"><path d="M1 6 L5 10 L13 1" stroke="var(--red)" stroke-width="3" fill="none"/></svg>Annual maintenance</li>
      <li><svg width="14" height="12" viewBox="0 0 14 12"><path d="M1 6 L5 10 L13 1" stroke="var(--red)" stroke-width="3" fill="none"/></svg>Pest control</li>
      <li><svg width="14" height="12" viewBox="0 0 14 12"><path d="M1 6 L5 10 L13 1" stroke="var(--red)" stroke-width="3" fill="none"/></svg>AC duct cleaning</li>
      <li><svg width="14" height="12" viewBox="0 0 14 12"><path d="M1 6 L5 10 L13 1" stroke="var(--red)" stroke-width="3" fill="none"/></svg>Remodeling</li>
    </ul>
    <p class="copy">GPS-dispatched technicians bring the right tools at the right time, day or night.</p>
  </section>

  <footer class="footer">
    <span class="footer-call">Call us now for a free estimate</span>
    <span class="footer-phone"><svg width="20" height="20" viewBox="0 0 22 22"><circle cx="11" cy="11" r="11" fill="var(--white)"/><path d="M7 5 L9 5 L10 8 L8.6 9.2 Q10 12 12.8 13.4 L14 12 L17 13 L17 15 Q16 17 14 17 Q6 15.5 5 7 Q5 5.5 7 5Z" fill="var(--green)"/></svg>800 GLEAMS</span>
  </footer>

</main>
</body>
</html>
```